Business card for auto dealership

Looking for a clean modern design.
Would like attached logo incorporated

Industry/Entity Type

Car dealership

Contact Information for Business Card

Name, website, phone, cell, fax, email

```html
<!DOCTYPE html>
<html lang="en">
<head>
<meta charset="utf-8">
<title>Harlow Truck &amp; Auto Sales – Business Card</title>
<link rel="stylesheet" href="https://fonts.googleapis.com/css2?family=Roboto:wght@400;500&display=swap">
<style>
  :root {
    --page: #e9eaec;
    --slate: #43546a;
    --white: #ffffff;
    --red: #a81c1c;
    --ink: #3d4654;
    --shadow: rgba(30, 36, 46, 0.18);
  }
  * { box-sizing: border-box; margin: 0; padding: 0; }
  html, body {
    width: 1200px;
    height: 900px;
    overflow: hidden;
    background: var(--page);
    font-family: "Roboto", Arial, sans-serif;
  }
  .sheet {
    position: relative;
    width: 1200px;
    height: 900px;
  }
  .card {
    position: absolute;
    left: 300px;
    width: 600px;
    height: 343px;
    border-radius: 16px;
    box-shadow: 0 6px 18px var(--shadow);
    overflow: hidden;
  }
  .card--front {
    top: 84px;
    background: var(--slate);
    display: flex;
    align-items: center;
    justify-content: center;
  }
  .card--back {
    top: 473px;
    background: var(--white);
  }
  .brand {
    font-weight: 500;
    text-align: center;
    line-height: 1.1;
  }
  .brand__name {
    display: block;
    font-size: 58px;
    letter-spacing: 1px;
  }
  .brand__tagline {
    display: block;
    font-size: 15px;
    letter-spacing: 3px;
    text-transform: uppercase;
  }
  .card--front .brand { color: var(--white); }
  .card--back .brand {
    position: absolute;
    left: 40px;
    top: 128px;
    width: 240px;
    color: var(--slate);
  }
  .card--back .brand__name { font-size: 44px; }
  .card--back .brand__tagline { font-size: 11.5px; letter-spacing: 2px; }
  .divider {
    position: absolute;
    left: 300px;
    top: 84px;
    width: 2px;
    height: 176px;
    background: var(--red);
  }
  .contact {
    position: absolute;
    left: 326px;
    top: 78px;
  }
  .contact__name {
    color: var(--red);
    font-size: 26px;
    font-weight: 500;
    letter-spacing: 0.5px;
    text-transform: uppercase;
  }
  .contact__role {
    color: var(--ink);
    font-size: 14px;
    letter-spacing: 1px;
    text-transform: uppercase;
    margin: 2px 0 14px;
  }
  .contact__list { list-style: none; }
  .contact__item {
    display: flex;
    align-items: center;
    gap: 10px;
    color: var(--ink);
    font-size: 15px;
    line-height: 26px;
  }
  .contact__icon {
    width: 13px;
    height: 13px;
    flex: none;
    color: var(--red);
  }
</style>
</head>
<body>
<main class="sheet">
  <section class="card card--front" aria-label="Card front">
    <div class="brand">
      <span class="brand__name">Harlow</span>
      <span class="brand__tagline">Truck &amp; Auto Sales</span>
    </div>
  </section>

  <section class="card card--back" aria-label="Card back">
    <div class="brand">
      <span class="brand__name">Harlow</span>
      <span class="brand__tagline">Truck &amp; Auto Sales</span>
    </div>
    <div class="divider"></div>
    <div class="contact">
      <h1 class="contact__name">Daniel Brooks</h1>
      <p class="contact__role">Director</p>
      <ul class="contact__list">
        <li class="contact__item">
          <svg class="contact__icon" viewBox="0 0 16 16" aria-hidden="true"><path fill="currentColor" d="M3.6 1.2l2.3 2.4-1.3 2a9 9 0 0 0 5.8 5.8l2-1.3 2.4 2.3-1.4 2.1C7.5 15.8.2 8.5 1.5 2.6z"/></svg>
          <span>+330 2450-1184</span>
        </li>
        <li class="contact__item">
          <svg class="contact__icon" viewBox="0 0 16 16" aria-hidden="true"><path fill="currentColor" d="M4 1h6l2 2v3H4zM1 7h14v6h-3v2H4v-2H1zm4 4v3h6v-3z"/></svg>
          <span>+330 2460-3392</span>
        </li>
        <li class="contact__item">
          <svg class="contact__icon" viewBox="0 0 16 16" aria-hidden="true"><path fill="none" stroke="currentColor" stroke-width="1.5" d="M1.5 3.5h13v9h-13zM1.5 3.5l6.5 5 6.5-5"/></svg>
          <span>info@harlowtruckauto.com</span>
        </li>
        <li class="contact__item">
          <svg class="contact__icon" viewBox="0 0 16 16" aria-hidden="true"><g fill="none" stroke="currentColor" stroke-width="1.3"><circle cx="8" cy="8" r="6.5"/><ellipse cx="8" cy="8" rx="3" ry="6.5"/><path d="M1.5 8h13M2.5 4.8h11M2.5 11.2h11"/></g></svg>
          <span>www.harlowtruckauto.com</span>
        </li>
      </ul>
    </div>
  </section>
</main>
</body>
</html>
```